New to ArtHively? This Contest is for you!

Are you new to ArtHively and looking to enter your first contest? Look no further! We're launching this special contest to help you get started on building a design portfolio at ArtHively!

Requirements:
* Create a beautiful and eye-catching graphic design which includes the words "Find me on ArtHively!"
* Upload your design to this contest AND share it on Chatterloop
* You must upload your entry before 12:00am 1 April
* This must be your very FIRST entry on ArtHively to be eligible to receive a prize. If you've already entered other ArtHively contests you won't be eligible to win the prizes
* Your design must adhere to our quality standards to be eligible to receive a prize

Prizes:
* There are 150 x $5 participation payments ($750) available to be awarded to high-quality designs
* First prize for the best design is $150
* Second prize is $100

Requirements
Must have
• Your design must contain the words "Find me on ArtHively".
• This must be your first entry on ArtHively to be eligible for the prizes.
• Your design must adhere to our quality standards.
Should not have
• No stock images or overused concepts.

```html
<!DOCTYPE html>
<html lang="en">
<head>
<meta charset="utf-8">
<title>Find me on ArtHively! – Daily puzzle</title>
<link rel="stylesheet" href="https://fonts.googleapis.com/css2?family=Open+Sans:wght@400;600&display=swap">
<style>
  :root {
    --bg: #f1ede6;
    --page-green: #a9c23f;
    --header-dark: #3a3c3a;
    --header-green: #b6d14a;
    --grid-white: #ffffff;
    --grid-line: #b9bcb6;
    --letter: #4a4d4a;
    --ink: #232323;
    --highlight: rgba(236, 240, 60, 0.75);
    --notes-line: #c9ccc6;
    --ink-soft: #d9d9d6;
  }
  * { box-sizing: border-box; margin: 0; padding: 0; }
  html, body { width: 1200px; height: 1000px; overflow: hidden; }
  body { background: var(--bg); font-family: "Open Sans", Arial, sans-serif; position: relative; }

  .puzzle-page {
    position: absolute; left: 270px; top: 40px;
    width: 660px; height: 920px;
    background: var(--page-green);
    box-shadow: 0 2px 10px rgba(0,0,0,0.15);
  }
  .page-header {
    height: 100px; background: var(--header-dark);
    display: flex; flex-direction: column; justify-content: center; align-items: flex-end;
    padding-right: 40px; color: var(--header-green);
  }
  .page-date { font-size: 20px; font-weight: 400; color: #e6ecd6; }
  .page-title { font-size: 32px; font-weight: 400; line-height: 1.2; }

  .word-search {
    position: absolute; left: 50px; top: 130px;
    width: 560px; height: 600px;
  }
  .letter-grid {
    display: grid; grid-template-columns: repeat(14, 40px); grid-auto-rows: 40px;
    background: var(--grid-white);
    border-top: 1px solid var(--grid-line); border-left: 1px solid var(--grid-line);
  }
  .letter-grid span {
    display: flex; align-items: center; justify-content: center;
    border-right: 1px solid var(--grid-line); border-bottom: 1px solid var(--grid-line);
    font-size: 20px; color: var(--letter);
  }
  .found-marks { position: absolute; inset: 0; pointer-events: none; }
  .found-marks .circled { fill: none; stroke: var(--ink); stroke-width: 2.5; }
  .found-marks .highlighted { fill: var(--highlight); }

  .notes-panel {
    position: absolute; left: 50px; top: 750px;
    width: 560px; height: 150px;
    background: var(--grid-white)
      repeating-linear-gradient(to bottom, transparent 0 23px, var(--notes-line) 23px 24px);
  }
  .notes-label { position: absolute; left: 8px; bottom: 4px; font-size: 12px; color: var(--letter); }
  .hand-lettering {
    position: absolute; left: 120px; top: 20px; width: 320px; height: 100px;
    background: linear-gradient(135deg, var(--ink-soft), #c5c5c2);
    border-radius: 6px;
  }
</style>
</head>
<body>
  <main class="puzzle-page">
    <header class="page-header">
      <p class="page-date">1 April 2015</p>
      <h1 class="page-title">Your daily puzzle</h1>
    </header>

    <section class="word-search" aria-label="Word search">
      <div class="letter-grid">
        <span>e</span><span>s</span><span>p</span><span>i</span><span>r</span><span>e</span><span>d</span><span>e</span><span>s</span><span>k</span><span>y</span><span>t</span><span>a</span><span>z</span>
        <span>o</span><span>e</span><span>a</span><span>n</span><span>o</span><span>n</span><span>e</span><span>n</span><span>t</span><span>x</span><span>e</span><span>a</span><span>n</span><span>x</span>
        <span>F</span><span>e</span><span>w</span><span>n</span><span>e</span><span>g</span><span>s</span><span>n</span><span>s</span><span>s</span><span>e</span><span>a</span><span>o</span><span>b</span>
        <span>i</span><span>t</span><span>n</span><span>d</span><span>c</span><span>a</span><span>i</span><span>t</span><span>u</span><span>r</span><span>e</span><span>a</span><span>l</span><span>p</span>
        <span>n</span><span>m</span><span>t</span><span>g</span><span>g</span><span>r</span><span>e</span><span>a</span><span>t</span><span>m</span><span>t</span><span>a</span><span>e</span><span>s</span>
        <span>d</span><span>e</span><span>o</span><span>p</span><span>c</span><span>i</span><span>n</span><span>a</span><span>m</span><span>t</span><span>a</span><span>k</span><span>s</span><span>w</span>
        <span>x</span><span>i</span><span>n</span><span>e</span><span>s</span><span>i</span><span>g</span><span>n</span><span>p</span><span>e</span><span>s</span><span>i</span><span>k</span><span>t</span>
        <span>a</span><span>s</span><span>e</span><span>A</span><span>r</span><span>t</span><span>H</span><span>i</span><span>v</span><span>e</span><span>l</span><span>y</span><span>o</span><span>x</span>
        <span>s</span><span>x</span><span>e</span><span>p</span><span>i</span><span>c</span><span>g</span><span>p</span><span>e</span><span>r</span><span>k</span><span>n</span><span>o</span><span>d</span>
        <span>r</span><span>d</span><span>e</span><span>x</span><span>t</span><span>e</span><span>a</span><span>m</span><span>w</span><span>o</span><span>r</span><span>k</span><span>a</span><span>x</span>
        <span>e</span><span>s</span><span>e</span><span>t</span><span>e</span><span>a</span><span>m</span><span>w</span><span>o</span><span>n</span><span>k</span><span>l</span><span>i</span><span>v</span>
        <span>p</span><span>e</span><span>r</span><span>c</span><span>u</span><span>R</span><span>o</span><span>w</span><span>a</span><span>n</span><span>l</span><span>t</span><span>e</span><span>a</span>
        <span>e</span><span>l</span><span>v</span><span>i</span><span>s</span><span>K</span><span>e</span><span>s</span><span>s</span><span>l</span><span>e</span><span>r</span><span>a</span><span>t</span>
        <span>c</span><span>w</span><span>t</span><span>a</span><span>l</span><span>e</span><span>n</span><span>t</span><span>s</span><span>i</span><span>s</span><span>a</span><span>u</span><span>p</span>
        <span>t</span><span>h</span><span>f</span><span>l</span><span>u</span><span>s</span><span>h</span><span>e</span><span>d</span><span>o</span><span>n</span><span>t</span><span>e</span><span>r</span>
      </div>
      <svg class="found-marks" width="560" height="600" viewBox="0 0 560 600" aria-hidden="true">
        <rect class="highlighted" x="202" y="448" width="196" height="26" rx="8"/>
        <rect class="highlighted" x="202" y="488" width="276" height="26" rx="8"/>
        <ellipse class="circled" cx="20" cy="160" rx="18" ry="82"/>
        <ellipse class="circled" cx="60" cy="200" rx="18" ry="42"/>
        <ellipse class="circled" cx="100" cy="240" rx="18" ry="42"/>
        <ellipse class="circled" cx="300" cy="300" rx="186" ry="19"/>
      </svg>
    </section>

    <section class="notes-panel">
      <div class="hand-lettering" role="img" aria-label="Hand-lettered marker text: Find me on ArtHively!"></div>
      <span class="notes-label">Notes</span>
    </section>
  </main>
</body>
</html>
```